New look and feel for investment website

Hi

Our website needs a crisp and professional look and feel applying to it. Here’s the address: http://www.brightplinth.co.uk. Since posting the brief yesterday (Tuesday, 16 August), we've reduced the amount of content on the home page, which should make life a little easier for you. We will come back later today, with some points of reference in terms of sites we like the look of. (See below)

17 August, 1.20pm GMT. OK, comments generally on the designs submitted so far. Please keep in mind that images of graphs, piles of coins, paper money and pretty females are not what is required. Better to think in terms of abstract imagery instead. Ratios? Circles? Relationships? Patterns? Not money,sex,graphs etc. Hope that helps.

For guidance on look and feel, please refer to these sites, which we like:

http://www.morvelle.co.uk/
http://www.qz.com/
https://www.harrowfieldtamsin.com
https://www.pirelconcerns.com
https://www.kvantule.com
Updates

Here's the Tall Beacons logo created in AI CS5.

Our market is professional financial advisers and relatively sophisticated private investors. The look and feel therefore should be slick and sophisticated - not 'lively' and lightweight, more like a banking site. Please read the brief again where we've added a list of websites that we really like the look of to get a better feel for what we're looking for. Thanks once again, we appreciate the work you're putting in.

It's essential that all the elements that are on the current home page be included on all new designs. 

We use a device in our e-mails which you may wish to incorporate in your design.

Target Market(s)

Professional financial advisers. People who know about investment and money.

Industry/Entity Type

Investment

Requirements
Should not have
• Graphs or people.

```html
<!DOCTYPE html>
<html lang="en">
<head>
<meta charset="utf-8">
<title>Tall Beacons – Value Investing</title>
<link href="https://fonts.googleapis.com/css2?family=Maven+Pro:wght@400;500;700&family=PT+Serif:ital,wght@0,400;1,400&family=Open+Sans:wght@400;600;700&display=swap" rel="stylesheet">
<style>
:root{
  --ink:#333;
  --ink-soft:#555;
  --accent-red:#e2173a;
  --accent-pink:#d8145a;
  --accent-green:#3aa53a;
  --accent-navy:#1a3c6e;
  --bar-top:#1d4f9c;
  --bar-bottom:#1aa3e8;
  --stat-circle:#4b5563;
  --panel:#e6e6e6;
  --orange:#f0a030;
  --placeholder-a:#f1ece6;
  --placeholder-b:#e6edf2;
}
*{box-sizing:border-box;margin:0;padding:0}
html,body{width:960px;height:1200px;overflow:hidden}
body{position:relative;background:#fff;font-family:"Open Sans",sans-serif;color:var(--ink)}
.abs{position:absolute}

.top-bar{left:0;top:0;width:960px;height:29px;background:repeating-linear-gradient(45deg,#4f4f4f 0 2px,#464646 2px 4px);display:flex;align-items:center;padding-left:98px;gap:23px}
.top-bar a{color:#eee;font-size:9.5px;text-decoration:none}

.brand{left:96px;top:50px;display:flex;align-items:center;gap:4px;font-family:"Maven Pro",sans-serif;font-size:29px;font-weight:500;color:#666;letter-spacing:-0.5px}
.brand-dot{width:6px;height:6px;background:var(--orange);border-radius:50%;margin-top:8px}
.tagline{right:96px;top:48px;width:400px;text-align:right;font-family:"PT Serif",serif;font-style:italic;font-size:13.6px;line-height:19px;color:#333}
.tagline em{color:var(--accent-red)}

.main-nav{left:96px;top:104px;width:768px;height:46px;border-top:1px solid #999;border-bottom:1px solid #ccc;display:flex;justify-content:space-between;padding:7px 12px 0}
.nav-item{display:flex;flex-direction:column;align-items:center;gap:3px;font-size:9px;color:var(--ink-soft)}
.nav-item svg{width:14px;height:14px}

.hero-art{left:118px;top:178px;width:326px;height:281px;background:linear-gradient(135deg,var(--placeholder-a),var(--placeholder-b))}
.hero-title{left:496px;top:232px;font-family:"Maven Pro",sans-serif;font-weight:400;font-size:29px;line-height:29px;color:#555;letter-spacing:.3px}
.hero-title em{font-style:italic}
.hero-sub{left:495px;top:334px;font-family:"Maven Pro",sans-serif;font-size:13px;line-height:17px;color:#222}
.hero-sub b{font-weight:500}
.cta{left:494px;top:386px;width:188px;height:34px;border:1px solid #ccc;border-radius:4px;background:linear-gradient(#fff,#e9e9e9);display:flex;align-items:center;padding-left:13px;gap:22px;font-family:"Maven Pro",sans-serif;font-size:16px;color:var(--accent-red)}

.divider{left:0;top:459px;width:960px;height:5px;background:#555}
.lower-bg{left:0;top:464px;width:960px;height:360px;background:linear-gradient(#e4e4e4,#f7f7f7 90px,#fff)}

.intro{left:96px;top:488px;width:358px}
.intro-head{display:flex;gap:8px;margin-bottom:8px}
.intro-head svg{flex-shrink:0}
.intro-head h2,.what-we-do h2{font-family:"Maven Pro",sans-serif;font-weight:400;font-size:15px;line-height:19px;color:var(--accent-pink)}
.body-copy{font-family:"PT Serif",serif;font-size:9.2px;line-height:16px;text-align:justify;color:#333;margin-bottom:16px}
.intro .body-copy:last-of-type{margin-bottom:8px}
.pull{font-family:"Maven Pro",sans-serif;font-size:12.5px;line-height:17px;color:var(--accent-navy)}

.what-we-do{left:492px;top:488px;width:372px}
.what-we-do h2{color:var(--accent-green);margin-bottom:7px}
.what-we-do .pull{margin:-2px 0 14px}
.more-link{display:inline-flex;align-items:center;gap:8px;font-size:10.5px;color:var(--accent-red);border-bottom:1px solid var(--accent-red);padding-bottom:3px}

.stats{left:96px;top:820px;width:768px;height:230px;background:var(--panel);border-top:1px solid #ccc;border-bottom:1px solid #bbb}

.contact-note{left:96px;top:1068px;width:768px;font-size:8.4px;line-height:13px;font-weight:700;color:#333}
.legal{left:96px;top:1120px;width:768px;font-size:7.3px;line-height:11.3px;color:#444}
</style>
</head>
<body>

<nav class="top-bar abs">
  <a href="#">Home</a><a href="#">Login</a><a href="#">Register for free</a><a href="#">Contact us</a><a href="#">Terms &amp; Conditions</a>
</nav>

<div class="brand abs">TallBeacons<span class="brand-dot"></span></div>
<p class="tagline abs">A potential return of <em>23.57 %</em> a year from America’s biggest businesses &nbsp;with the emphasis firmly on capital preservation.</p>

<nav class="main-nav abs">
  <span class="nav-item"><svg viewBox="0 0 14 14"><circle cx="7" cy="7" r="5.5" fill="none" stroke="#e2173a" stroke-width="1.5"/><path d="M7 4v3h2.5" stroke="#e2173a" stroke-width="1.5" fill="none"/></svg>2 Minute Guide</span>
  <span class="nav-item"><svg viewBox="0 0 14 14"><rect x="1" y="8" width="2.5" height="5" fill="#e2173a"/><rect x="4.5" y="5" width="2.5" height="8" fill="#e2173a"/><rect x="8" y="7" width="2.5" height="6" fill="#e2173a"/><rect x="11" y="2" width="2.5" height="11" fill="#e2173a"/></svg>Performance</span>
  <span class="nav-item"><svg viewBox="0 0 14 14"><ellipse cx="7" cy="7" rx="6" ry="3.5" fill="none" stroke="#e2173a" stroke-width="1.4"/><circle cx="7" cy="7" r="1.7" fill="#e2173a"/></svg>Watchlist</span>
  <span class="nav-item"><svg viewBox="0 0 14 14"><rect x="2" y="2" width="10" height="10" rx="1.5" fill="#f0a030"/><path d="M5 9l4-4" stroke="#fff" stroke-width="1.4"/></svg>Key Numbers</span>
  <span class="nav-item"><svg viewBox="0 0 14 14"><circle cx="7" cy="7.5" r="5.5" fill="#d4d21a"/><path d="M8 1v6h6A6 6 0 0 0 8 1z" fill="#f0c020"/></svg>Results</span>
  <span class="nav-item"><svg viewBox="0 0 14 14"><path d="M1 13l3-7 3 4 3-8 3 11z" fill="#3aa53a"/></svg>Trading History</span>
  <span class="nav-item"><svg viewBox="0 0 14 14"><circle cx="5.5" cy="5.5" r="3.8" fill="none" stroke="#2a9a5a" stroke-width="1.8"/><path d="M8.5 8.5L13 13" stroke="#2a9a5a" stroke-width="2.2"/></svg>FAQs</span>
  <span class="nav-item"><svg viewBox="0 0 14 14"><circle cx="5" cy="5" r="3.5" fill="#1a8ad8"/><circle cx="10" cy="9.5" r="3" fill="#1aa3e8"/></svg>Analysis</span>
  <span class="nav-item"><svg viewBox="0 0 14 14"><text x="7" y="12.5" text-anchor="middle" font-family="Open Sans,sans-serif" font-size="14" font-weight="700" fill="#1a5ab8">$</text></svg>Value Investing</span>
  <span class="nav-item"><svg viewBox="0 0 14 14"><path d="M1.5 1v11.5H13" stroke="#3a4a9a" stroke-width="1.4" fill="none"/><path d="M3 10l3-4 3 2 4-5" stroke="#3a4a9a" stroke-width="1.4" fill="none"/></svg>Castellan 1000 &amp; Meridian 500</span>
</nav>

<div class="hero-art abs" role="img" aria-label="Abstract illustration of multicoloured dots radiating from a central point"></div>

<h1 class="hero-title abs">We use Custom Software<br>to <em>analyse and identify</em><br>undervalued stocks</h1>
<p class="hero-sub abs">Monitor our service<br><b>free of charge for six months</b></p>
<a class="cta abs">Register for Free
  <svg width="10" height="13" viewBox="0 0 10 13"><path d="M2 1.5l5 5-5 5" stroke="var(--orange)" stroke-width="2.6" fill="none"/></svg>
</a>

<div class="divider abs"></div>
<div class="lower-bg abs"></div>

<section class="intro abs">
  <div class="intro-head">
    <svg width="34" height="50" viewBox="0 0 34 50"><g fill="#aaa"><rect x="24" y="0" width="8" height="8"/><rect x="14" y="12" width="8" height="8"/><rect x="0" y="22" width="8" height="8"/><rect x="0" y="34" width="32" height="2"/><rect x="0" y="40" width="32" height="2"/><rect x="0" y="46" width="32" height="2"/></g><path d="M28 8v8h-6M18 20v6H8" stroke="#aaa" fill="none"/></svg>
    <h2>A methodical, consistent, highly selective system-driven process for identifying, and investing in, undervalued stocks.</h2>
  </div>
  <p class="body-copy">The attractions of value investing need no explanation to those who subscribe to the concept. But it's impractical, if not impossible, for the private investor to implement the strategy (using direct holdings as distinct to collective funds) consistently. Although the data may be available, to undertake fundamental analysis regularly, on a reasonable number of stocks, entails a significant amount of time and effort.</p>
  <p class="body-copy">By definition - and depending on where you look and market conditions - undervalued businesses (stocks) are relatively scarce. So where does the value investor begin their search? Which and how many businesses must be scrutinised before one undervalued entity is found? And having identified a stock that's trading at less than its fair value, will that be the case next week or next month? Fundamentals can change for the worse at any time, so without the benefit of regular analysis, how will the value investor know when to disinvest?</p>
  <p class="pull">Those problems - and others - are now solved. Our software produces the quantitative analysis value investors need.</p>
</section>

<section class="what-we-do abs">
  <h2>Here's what we do:</h2>
  <p class="body-copy" style="text-align:left">Once a month, month in month out, our program scrutinises the key fundamentals of 1,000 large cap American companies which between them account for 92% of the US securities market.</p>
  <p class="body-copy" style="text-align:left">First of all, the program sifts through each of the 1,000 stocks searching for favourable arrays of fundamentals: that process usually filters out between 950 and 975 stocks. The software then applies a range of algorithms to the short-listed stocks to identify any which are trading at 35% (or more) below their estimated fair value. There are times when not one single stock on the shortlist satisfies that criteria. But when they do - and if there's room - those stocks are added to our portfolio.</p>
  <p class="pull">We're not stock pickers, share tippers or brokers. What we do is use software to analyse and identify stocks that appear to be undervalued.</p>
  <a class="more-link">More about value investing - the investment strategy we follow
    <svg width="18" height="8" viewBox="0 0 18 8"><path d="M0 4h16M12 1l4 3-4 3" stroke="#444" fill="none"/></svg>
  </a>
</section>

<section class="stats abs">
  <svg width="768" height="230" viewBox="0 0 768 230" font-family="Open Sans,sans-serif">
    <defs>
      <linearGradient id="barFill" x1="0" y1="0" x2="0" y2="1"><stop offset="0" stop-color="var(--bar-top)"/><stop offset="1" stop-color="var(--bar-bottom)"/></linearGradient>
    </defs>
    <line x1="10" y1="152" x2="383" y2="152" stroke="#444"/>
    <g fill="url(#barFill)">
      <rect x="32" y="106" width="29" height="46"/>
      <rect x="105" y="125" width="29" height="27"/>
      <rect x="170" y="152" width="29" height="6"/>
      <rect x="240" y="48" width="29" height="104"/>
      <rect x="315" y="106" width="29" height="46"/>
    </g>
    <g stroke="var(--accent-red)" stroke-width="1.5">
      <line x1="32" y1="106" x2="61" y2="106"/><line x1="105" y1="125" x2="134" y2="125"/><line x1="240" y1="48" x2="269" y2="48"/><line x1="315" y1="106" x2="344" y2="106"/>
    </g>
    <g fill="var(--accent-red)" font-size="13" font-weight="600" text-anchor="middle">
      <text x="53" y="100">23.57 <tspan font-weight="400">%</tspan></text>
      <text x="125" y="120">13.49 <tspan font-weight="400">%</tspan></text>
      <text x="188" y="143">-1.48 <tspan font-weight="400">%</tspan></text>
      <text x="259" y="44">69.77 <tspan font-weight="400">%</tspan></text>
      <text x="334" y="100">24.44 <tspan font-weight="400">%</tspan></text>
    </g>
    <g fill="#222" font-size="10" text-anchor="middle">
      <text x="45" y="173">Average,<tspan x="45" dy="11.5">annualised</tspan><tspan x="45" dy="11.5">compound</tspan><tspan x="45" dy="11.5">return:</tspan></text>
      <text x="118" y="173">YTD<tspan x="118" dy="11.5">Portfolio</tspan><tspan x="118" dy="11.5">Return</tspan></text>
      <text x="185" y="173">Highest<tspan x="185" dy="11.5">annual</tspan><tspan x="185" dy="11.5">loss</tspan></text>
      <text x="255" y="173">Highest<tspan x="255" dy="11.5">annual</tspan><tspan x="255" dy="11.5">gain</tspan></text>
      <text x="332" y="173">Average<tspan x="332" dy="11.5">return</tspan><tspan x="332" dy="11.5">per trade</tspan></text>
    </g>

    <g fill="var(--stat-circle)">
      <circle cx="450" cy="32" r="21"/><circle cx="450" cy="85" r="21"/><circle cx="450" cy="135" r="21"/>
    </g>
    <g fill="#fff" font-weight="700" text-anchor="middle">
      <text x="450" y="38" font-size="15"><tspan dy="-4">11</tspan><tspan dy="4">/4</tspan></text>
      <text x="450" y="92" font-size="19">5</text>
      <text x="450" y="141" font-size="16">287</text>
    </g>
    <g fill="#333" font-size="10">
      <text x="491" y="40">Maximum number of winning/losing trades in a row</text>
      <text x="491" y="95">The average number of trades a yearand never more<tspan x="491" dy="11">than five holdings at any one time</tspan></text>
      <text x="491" y="149">The average number of days a stock stays in the portfolio</text>
    </g>
    <g stroke="#777" stroke-dasharray="2 2">
      <line x1="491" y1="46" x2="762" y2="46"/><line x1="491" y1="118" x2="762" y2="118"/><line x1="491" y1="157" x2="762" y2="157"/>
    </g>
    <g fill="#222" font-size="10">
      <text x="436" y="180">86 trades</text>
      <text x="436" y="194">65 were profitable</text>
    </g>
    <rect x="493" y="175" width="268" height="6" fill="#1aa84a"/>
    <rect x="553" y="189" width="208" height="6" fill="#1a90d8"/>
    <text x="434" y="219" fill="var(--accent-red)" font-size="14.4">75.5 % success rate</text>
  </svg>
</section>

<p class="contact-note abs">If you have any questions, please e-mail info@brightplinth.co.uk. Although we’re very willing to answer queries about the way we pick stocks, please do keep in mind that as we’re giving this service away free of charge initially, we’re not inclined to expend time and energy debating the relative merits of value investing or fundamental analyses. Other than that, fire away!</p>

<p class="legal abs">This website is published by Tall Beacons Ltd. Registered in England No. 08314729. Registered office: 48 Larkfield Row London N7 2QD. This website and its content is the copyright of Tall Beacons Ltd - © Tall Beacons Ltd 2011. All rights reserved. Any redistribution or reproduction of part or all of the contents in any form is prohibited other than the following: you may print or download to a local hard disk extracts for your personal and non-commercial use only you may copy the content to individual third parties for their personal use, but only if you acknowledge the website as the source of the material. You may not, except with our express written permission, distribute or commercially exploit the content. Nor may you transmit it or store it in any other website or other form of electronic retrieval system.</p>

</body>
</html>
```